Business Card Design

Electrical Contracting buisness
need a buisness card relating to that buisness

Reason: Just need to discuss with partner

Industry/Entity Type

Business

Contact Information for Business Card

Colin Harbage Electrical
0417 562 983
colinharbage7@mailvessel.com
REC 48761

```html
<!DOCTYPE html>
<html lang="en">
<head>
<meta charset="utf-8">
<title>Colin Harbage Electrical – Business Card</title>
<link rel="stylesheet" href="https://fonts.googleapis.com/css2?family=Comfortaa:wght@400;600&display=swap">
<style>
  :root {
    --backdrop: #d6d3cf;
    --card-dark: #1c1c1c;
    --card-dark-edge: #2e2e2e;
    --band-white: #ffffff;
    --accent-yellow: #f2e600;
    --name-white: #f4f4f4;
    --ink: #2a2a2a;
  }
  html, body {
    margin: 0;
    padding: 0;
    width: 1200px;
    height: 1000px;
    overflow: hidden;
    background: var(--backdrop);
  }
  .canvas {
    position: relative;
    width: 1200px;
    height: 1000px;
    display: flex;
    align-items: center;
    justify-content: center;
  }
  .business-card {
    width: 700px;
    height: 400px;
    box-shadow: 0 14px 40px rgba(0,0,0,0.28);
  }
  .business-card svg { display: block; }
  .company-name {
    font-family: "Comfortaa", sans-serif;
    font-weight: 400;
    font-size: 30px;
    fill: var(--name-white);
  }
  .contact-line {
    font-family: "Comfortaa", sans-serif;
    font-weight: 600;
    font-size: 21px;
    fill: var(--ink);
  }
</style>
</head>
<body>
<main class="canvas">
  <div class="business-card">
    <svg width="700" height="400" viewBox="0 0 700 400" xmlns="http://www.w3.org/2000/svg">
      <defs>
        <linearGradient id="card-surface" x1="0" y1="0" x2="1" y2="1">
          <stop offset="0" stop-color="var(--card-dark-edge)"/>
          <stop offset="1" stop-color="var(--card-dark)"/>
        </linearGradient>
      </defs>
      <rect class="card-base" width="700" height="400" fill="url(#card-surface)"/>

      <path class="accent-stripe top" d="M0,86 Q350,116 700,186" fill="none" stroke="var(--accent-yellow)" stroke-width="5"/>
      <path class="white-band" d="M0,100 Q350,130 700,200 L700,330 Q350,350 0,310 Z" fill="var(--band-white)"/>
      <path class="accent-stripe bottom" d="M0,326 Q350,366 700,346" fill="none" stroke="var(--accent-yellow)" stroke-width="5"/>

      <rect class="name-marker" x="478" y="18" width="16" height="16" fill="var(--accent-yellow)"/>
      <text class="company-name" x="670" y="74" text-anchor="end">Colin Harbage Electrical</text>

      <g class="contact-details" text-anchor="middle">
        <text class="contact-line" x="360" y="208">0417 562 983</text>
        <text class="contact-line" x="360" y="242">colinharbage7@mailvessel.com</text>
        <text class="contact-line" x="360" y="276">REC 48761</text>
      </g>
    </svg>
  </div>
</main>
</body>
</html>
```